Tarnby Group letterhead

Hi,

I need a letterhead template created for our business. This should be done in word format and A4 size. The images need to not move in the template ie when I am adding writing in etc. and should flow on when I get to a second page.

I have attached our logo templates below.

Other details to include on the letterhead somewhere are:

0438 915 267
Max@Tarnbyelectrical.example.au
PO Box 817 Marrowvale NSW 2190
ABN: 57 318 962 407

Thanks!

```html
<!DOCTYPE html>
<html lang="en">
<head>
<meta charset="utf-8">
<title>Tarnby Group Letterhead</title>
<link rel="stylesheet" href="https://fonts.googleapis.com/css2?family=Montserrat:wght@400;700&display=swap">
<style>
  :root {
    --backdrop: #dcdedd;
    --paper: #ffffff;
    --ink: #1c1c1c;
    --accent: #e8541c;
  }
  * { box-sizing: border-box; margin: 0; padding: 0; }
  html, body {
    width: 1200px; height: 1200px; overflow: hidden;
    background: var(--backdrop);
    font-family: "Montserrat", sans-serif;
    color: var(--ink);
  }
  .sheet {
    position: absolute; left: 228px; top: 67px;
    width: 755px; height: 1066px;
    background: var(--paper);
  }
  .brand-mark {
    position: absolute; left: 234px; top: 106px;
    width: 66px; height: 66px; border-radius: 50%;
    border: 4px solid var(--ink);
  }
  .brand-name {
    position: absolute; left: 316px; top: 118px;
    font-weight: 700; font-size: 22px; line-height: 24px;
    letter-spacing: 1.5px; text-transform: uppercase;
    color: var(--ink); white-space: nowrap;
  }
  .brand-name .legal {
    display: block; font-size: 12px; line-height: 16px;
    letter-spacing: 4px; margin-top: 2px; padding-left: 2px;
  }
  .rule {
    position: absolute; left: 92px; width: 571px; height: 3px;
    background: var(--ink);
  }
  .rule-top { top: 188px; }
  .rule-bottom { top: 905px; }
  .contact-row {
    position: absolute; left: 0; right: 0;
    display: flex; justify-content: center; align-items: center;
    font-size: 14px; font-weight: 400; white-space: nowrap;
    line-height: 19px;
  }
  .contact-row.first { top: 920px; gap: 28px; }
  .contact-row.second { top: 950px; gap: 40px; }
  .item { display: inline-flex; align-items: center; }
  .icon {
    width: 19px; height: 19px; border-radius: 50%;
    background: var(--accent);
    display: inline-flex; align-items: center; justify-content: center;
    margin-right: 9px; flex: none;
  }
  .icon svg { width: 11px; height: 11px; }
</style>
</head>
<body>
  <main class="sheet">
    <header>
      <span class="brand-mark" aria-hidden="true"></span>
      <div class="brand-name">Tarnby Group<span class="legal">Pty Ltd</span></div>
    </header>
    <div class="rule rule-top"></div>

    <div class="rule rule-bottom"></div>
    <div class="contact-row first">
      <span class="item">
        <span class="icon"><svg viewBox="0 0 12 12"><path d="M6 1a3.5 3.5 0 0 0-3.5 3.5C2.5 7 6 11 6 11s3.5-4 3.5-6.5A3.5 3.5 0 0 0 6 1zm0 4.8a1.3 1.3 0 1 1 0-2.6 1.3 1.3 0 0 1 0 2.6z" fill="#fff"/></svg></span>
        PO Box 817 Marrowvale NSW 2190
      </span>
      <span class="item">ABN: 57 318 962 407</span>
    </div>
    <div class="contact-row second">
      <span class="item">
        <span class="icon"><svg viewBox="0 0 12 12"><path d="M3 1.5l1.8 2.2-1 1.1a6 6 0 0 0 3.4 3.4l1.1-1L10.5 9l-1 1.5C5.5 10.5 1.5 6.5 1.5 2.5z" fill="#fff"/></svg></span>
        (0438) 915 267
      </span>
      <span class="item">
        <span class="icon"><svg viewBox="0 0 12 12" fill="none" stroke="#fff" stroke-width="1"><circle cx="6" cy="6" r="4.5"/><ellipse cx="6" cy="6" rx="2" ry="4.5"/><path d="M1.5 6h9M2.3 3.6h7.4M2.3 8.4h7.4"/></svg></span>
        Max@Tarnbyelectrical.example.au
      </span>
    </div>
  </main>
</body>
</html>
```